I am a home builder and developer

I would like some sort of architectural design like a pencil type of drawing of a house but want it to be professional looking and two sided.

Simply I am a custom home builder and land developer. I would like a new design other than what I have now that's what I thought y'all did. I like mostly black maybe with an pencil type of drawing of a house. Like an architectural look.

Industry/Entity Type

Home Builder

```html
<!DOCTYPE html>
<html lang="en">
<head>
<meta charset="utf-8">
<title>R &amp; T Building Inc — Business Card</title>
<link rel="stylesheet" href="https://fonts.googleapis.com/css2?family=Manrope:wght@400;500;600;800&display=swap">
<style>
  :root {
    --backdrop: #e8e5e1;
    --card: #ffffff;
    --ink: #2a2a2a;
    --ink-soft: #6b6b6b;
    --rule: #8a8a8a;
    --sketch-light: #f2f2f2;
    --sketch-dark: #c9c9c9;
  }
  * { box-sizing: border-box; margin: 0; padding: 0; }
  html, body {
    width: 1200px; height: 1000px; overflow: hidden;
    background: var(--backdrop);
    font-family: "Manrope", sans-serif;
    color: var(--ink);
  }
  .canvas { position: relative; width: 1200px; height: 1000px; }
  .card {
    position: absolute; left: 266px;
    width: 666px; height: 397px;
    background: var(--card);
    box-shadow: 0 3px 10px rgba(0,0,0,0.18);
  }
  .card--front { top: 74px; }
  .card--back { top: 533px; }
  .card__frame { position: absolute; inset: 0; }
  .house-sketch {
    position: absolute; left: 77px; top: 109px;
    width: 213px; height: 113px;
    background: radial-gradient(ellipse at 50% 55%, var(--sketch-light) 30%, var(--sketch-dark) 100%);
    border-radius: 4px;
  }
  .company {
    position: absolute; left: 40px; top: 236px; width: 294px;
    text-align: center; font-weight: 500; color: var(--ink);
  }
  .company__name { font-size: 28px; letter-spacing: 0.2px; line-height: 1; }
  .company__suffix { font-size: 17px; margin-top: 8px; padding-left: 8px; line-height: 1; }
  .contact { position: absolute; left: 362px; top: 122px; }
  .contact__name { font-size: 21px; font-weight: 500; letter-spacing: 0.3px; line-height: 1; }
  .contact__name strong { font-weight: 800; }
  .contact__role { font-size: 16px; font-weight: 600; color: var(--ink-soft); margin-top: 9px; }
  .contact__list { list-style: none; margin-top: 48px; }
  .contact__item {
    display: flex; align-items: center; gap: 5px;
    font-size: 16px; font-weight: 500; color: var(--ink-soft); height: 29px;
  }
  .contact__icon { width: 15px; height: 15px; fill: var(--ink); flex: none; }
</style>
</head>
<body>
<main class="canvas">
  <section class="card card--front">
    <svg class="card__frame" width="666" height="397" aria-hidden="true">
      <g stroke="var(--rule)" stroke-width="1.5">
        <line x1="20" y1="32" x2="652" y2="32"/>
        <line x1="20" y1="365" x2="652" y2="365"/>
        <line x1="32" y1="14" x2="32" y2="378"/>
        <line x1="634" y1="14" x2="634" y2="378"/>
      </g>
    </svg>
    <div class="house-sketch" role="img" aria-label="Pencil-style architectural sketch of a two-storey house"></div>
    <div class="company">
      <div class="company__name">R &amp; T BUILDING</div>
      <div class="company__suffix">INC</div>
    </div>
    <div class="contact">
      <h1 class="contact__name"><strong>ELLIS</strong> HARLOW</h1>
      <p class="contact__role">Architect</p>
      <ul class="contact__list">
        <li class="contact__item">
          <svg class="contact__icon" viewBox="0 0 24 24" aria-hidden="true"><path d="M6.6 10.8a15.1 15.1 0 0 0 6.6 6.6l2.2-2.2c.3-.3.7-.4 1-.2 1.1.4 2.3.6 3.6.6.6 0 1 .4 1 1V20c0 .6-.4 1-1 1A17 17 0 0 1 3 4c0-.6.4-1 1-1h3.5c.6 0 1 .4 1 1 0 1.3.2 2.5.6 3.6.1.3 0 .7-.2 1z"/></svg>
          555-014-2287
        </li>
        <li class="contact__item">
          <svg class="contact__icon" viewBox="0 0 24 24" aria-hidden="true"><path d="M2 5h20v14H2z M3.5 6.5 12 12.5l8.5-6" fill="var(--ink)" stroke="#fff" stroke-width="1.4"/></svg>
          hello@rtbuildinginc.com
        </li>
      </ul>
    </div>
  </section>

  <section class="card card--back">
    <svg class="card__frame" width="666" height="397" aria-hidden="true">
      <g stroke="var(--rule)" stroke-width="1.5">
        <line x1="20" y1="32" x2="652" y2="32"/>
        <line x1="20" y1="365" x2="652" y2="365"/>
        <line x1="32" y1="14" x2="32" y2="378"/>
        <line x1="634" y1="14" x2="634" y2="378"/>
      </g>
    </svg>
    <div class="house-sketch" role="img" aria-label="Pencil-style architectural sketch of a two-storey house"></div>
    <div class="company">
      <div class="company__name">R &amp; T BUILDING</div>
      <div class="company__suffix">INC</div>
    </div>
    <div class="contact">
      <h2 class="contact__name"><strong>ELLIS</strong> HARLOW</h2>
      <p class="contact__role">Architect</p>
      <ul class="contact__list">
        <li class="contact__item">
          <svg class="contact__icon" viewBox="0 0 24 24" aria-hidden="true"><path d="M6.6 10.8a15.1 15.1 0 0 0 6.6 6.6l2.2-2.2c.3-.3.7-.4 1-.2 1.1.4 2.3.6 3.6.6.6 0 1 .4 1 1V20c0 .6-.4 1-1 1A17 17 0 0 1 3 4c0-.6.4-1 1-1h3.5c.6 0 1 .4 1 1 0 1.3.2 2.5.6 3.6.1.3 0 .7-.2 1z"/></svg>
          555-014-2287
        </li>
        <li class="contact__item">
          <svg class="contact__icon" viewBox="0 0 24 24" aria-hidden="true"><path d="M2 5h20v14H2z M3.5 6.5 12 12.5l8.5-6" fill="var(--ink)" stroke="#fff" stroke-width="1.4"/></svg>
          hello@rtbuildinginc.com
        </li>
      </ul>
    </div>
  </section>
</main>
</body>
</html>
```